New image for luxury travel blog

I would like to refresh my blog and social media platforms and would require a new design concept for lilyfarwander.net. I will require the following:

- Top banner for website using current size
- Similar imagery for Facebook Page, Twitter Profile, Google Plus (page and personal profile)
- New profile photo (for each social platform) in appropriate sizes for each platform (with white round shape as I currently have), and 2-3 larger options (500x500, 250x250px)
- Artwork for business card (pavex.net)
- A square logo (based on image defined) for Lily Far Wander Notes (that can be used as an ad of just when I need a logo of the blog)
- Copy to use - Lily Far Wander Notes - a luxury travel blog by Beth Kowal Trenholm.
- Current tagline 'Pack light. Meet kin. Wear heels.' should also be used, but suggestions welcome.
- I am partial to a shade of blue

Feel free to use any photo you can find on my blog at http://lilyfarwander.net which you may find appropriate.

```html
<!DOCTYPE html>
<html lang="en">
<head>
<meta charset="UTF-8">
<title>Lily Far Wander Notes</title>
<link rel="stylesheet" href="https://fonts.googleapis.com/css2?family=Cutive+Mono&display=swap">
<style>
  :root {
    --sky-orange: #f2a865;
    --sky-orange-light: #f4ae6d;
    --landscape-top: #8f6a2c;
    --landscape-mid: #7d5a22;
    --landscape-deep: #6a4c1c;
    --portrait-dark: #3a2a22;
    --portrait-warm: #b07a5c;
    --text-white: #ffffff;
    --rule-white: rgba(255, 255, 255, 0.75);
    --accent-blue: #1f5a86;
  }
  html, body {
    margin: 0;
    padding: 0;
    width: 1200px;
    height: 1200px;
    overflow: hidden;
    background: var(--sky-orange);
  }
  .banner {
    position: relative;
    width: 1200px;
    height: 1200px;
    overflow: hidden;
    background: linear-gradient(180deg, var(--sky-orange-light) 0%, var(--sky-orange) 70%);
    font-family: "Cutive Mono", "Courier New", monospace;
  }
  .landscape-photo {
    position: absolute;
    left: 0;
    top: 780px;
    width: 1200px;
    height: 414px;
    background: linear-gradient(180deg, var(--landscape-top) 0%, var(--landscape-mid) 45%, var(--landscape-deep) 100%);
  }
  .accent-strip {
    position: absolute;
    left: 0;
    bottom: 0;
    width: 1200px;
    height: 6px;
    background: var(--accent-blue);
  }
  .portrait {
    position: absolute;
    left: 244px;
    top: 25px;
    width: 704px;
    height: 704px;
    border-radius: 50%;
    background: radial-gradient(circle at 52% 45%, var(--portrait-warm) 0%, #8a5a44 35%, var(--portrait-dark) 75%);
  }
  .blog-title {
    position: absolute;
    left: 0;
    top: 888px;
    width: 1200px;
    margin: 0;
    text-align: center;
    color: var(--text-white);
    font-size: 52px;
    font-weight: 400;
    letter-spacing: 0.38em;
    padding-left: 0.38em;
    box-sizing: border-box;
    text-transform: uppercase;
    line-height: 1;
    white-space: nowrap;
  }
  .title-rule {
    position: absolute;
    left: 0;
    top: 964px;
    width: 1200px;
    height: 1px;
    background: var(--rule-white);
  }
  .blog-subtitle {
    position: absolute;
    left: 0;
    top: 994px;
    width: 1200px;
    margin: 0;
    text-align: center;
    color: var(--text-white);
    font-size: 27px;
    letter-spacing: 0.2em;
    line-height: 1;
    white-space: nowrap;
  }
  .blog-tagline {
    position: absolute;
    left: 0;
    top: 1100px;
    width: 1200px;
    margin: 0;
    text-align: center;
    color: var(--text-white);
    font-size: 27px;
    letter-spacing: 0.2em;
    line-height: 1;
    white-space: nowrap;
  }
</style>
</head>
<body>
  <main class="banner">
    <div class="landscape-photo" role="img" aria-label="Photo of a wooded treeline and fields in warm sunset tones"></div>
    <div class="accent-strip"></div>
    <div class="portrait" role="img" aria-label="Round portrait photo of the blog author laughing"></div>
    <h1 class="blog-title">Lily Far Wander Notes</h1>
    <div class="title-rule"></div>
    <p class="blog-subtitle">A luxury travel blog by Beth Kowal Trenholm.</p>
    <p class="blog-tagline">Pack light. Meet kin. Wear heels.</p>
  </main>
</body>
</html>
```